Redesign of page from emergency manual

Please redesign this PDF to look better. Please don't include any stock photos. It must be legible. Making some words bold is probably a good idea.

Here are some things I like :

https://brambolthouse.com.au/collections/frontpage/products/the-kvt-v2-ebook

https://media-qz.fennowstatic.net/kd-pqRwTbnVYy_ZaWsLmHu400K4sa-Xe9vbPqTn37sJdVRwaT4PiedfxrmZ8NTcUjK=w1052-h592-rw

```html
<!DOCTYPE html>
<html lang="en">
<head>
<meta charset="utf-8">
<title>Hypertension, Acute</title>
<link rel="stylesheet" href="https://fonts.googleapis.com/css2?family=Open+Sans:ital,wght@0,400;0,600;0,700;0,800;1,400&display=swap">
<style>
:root{
  --bg:#f2f2f2;
  --ink:#111;
  --cyan:#66e8fb;
  --cyan-light:#b6f3fc;
  --blue-pill:#a8dce8;
  --sky:#2fa8e0;
  --lime:#8dc63f;
  --green:#3db54a;
  --red:#e4212a;
  --row-head:#fdebc4;
  --row-1:#fce8a5;
  --row-2:#fdb06e;
  --row-3:#f47a5e;
  --white:#fff;
  --grey:#8a8a8a;
  --pulse:#d6d6d6;
}
*{box-sizing:border-box;margin:0;padding:0}
html,body{width:1200px;height:927px;overflow:hidden;background:var(--bg)}
body{font-family:"Open Sans",sans-serif;color:var(--ink);position:relative;letter-spacing:.5px}
.abs{position:absolute}
.title{left:249px;top:14px;font-size:54px;font-weight:800;letter-spacing:1px;line-height:1;white-space:nowrap;display:flex;align-items:center}
.title-mark{display:inline-block;width:42px;height:42px;margin:0 3px;border-radius:8px;background:linear-gradient(135deg,var(--red),#b8141b)}
.subtitle{left:288px;top:66px;font-size:18px;white-space:nowrap;letter-spacing:.6px}
.pulse{height:76px;background:linear-gradient(90deg,transparent,var(--pulse) 30%,var(--pulse) 70%,transparent);opacity:.7}
.pulse-left{left:0;top:42px;width:270px}
.pulse-right{left:928px;top:42px;width:215px}
.side-band{left:1143px;top:0;width:57px;height:927px;background:var(--cyan)}
.side-title{left:1173px;top:207px;transform-origin:0 0;transform:rotate(90deg) translateY(-50%);font-size:27px;font-weight:800;white-space:nowrap;display:flex;align-items:center}
.side-title .title-mark{width:20px;height:20px;border-radius:4px;margin:0 2px}
.revision{left:1178px;top:762px;transform-origin:0 0;transform:rotate(90deg) translateY(-100%);font-size:14px;color:var(--grey);white-space:nowrap}
.child-icon{left:36px;top:129px;width:63px;height:63px;border-radius:50%;background:linear-gradient(var(--row-2),var(--sky))}
.peds{left:112px;top:124px;width:535px;font-size:20px;line-height:23.5px}
.peds b{color:var(--sky)}
.tip-icon{width:71px;height:55px;border-radius:14px;display:flex;align-items:center;justify-content:center}
.tip-text{left:191px;width:448px;height:55px;border-radius:14px;color:var(--white);font-size:19.5px;line-height:23px;padding:4px 15px}
.lime{background:var(--lime)}
.green{background:var(--green)}
.note{left:121px;top:330px;font-size:20px;font-style:italic}
.bp-head{left:681px;top:123px;width:423px;height:39px;border-radius:20px;background:var(--blue-pill);font-size:19px;font-weight:700;text-align:center;line-height:39px}
.bp-head span{color:var(--red)}
.bp-table{left:681px;top:169px;width:423px;border-radius:30px 30px 40px 40px;overflow:hidden}
.bp-row{display:grid;grid-template-columns:136px 144px 143px;gap:0 3px;margin-bottom:2px;font-size:19px;text-align:center}
.bp-row>div{display:flex;align-items:center;justify-content:center}
.r-head{height:47px;background:var(--row-head);font-weight:700}
.r1{height:36px;background:var(--row-1)}
.r2{height:36px;background:var(--row-2)}
.r3{height:45px;background:var(--row-3);padding-bottom:8px}
.caution-label{left:45px;top:358px;font-size:20px;font-weight:700;color:var(--red)}
.caution{left:84px;top:388px;width:1045px;font-size:19.5px;line-height:24px;letter-spacing:.45px}
.panel{background:var(--white);border-radius:30px}
.action-panel{left:90px;top:516px;width:321px;height:369px}
.drug-panel{left:427px;top:516px;width:696px;height:371px}
.pill{height:51px;border-radius:25px;font-weight:700;text-align:center}
.action-head{left:107px;top:480px;width:288px;background:var(--cyan-light);font-size:25px;line-height:51px}
.drug-head{left:438px;top:480px;width:674px;background:var(--cyan);font-size:20px;line-height:45px}
.divider{left:121px;width:938px;height:1px;background:var(--ink)}
.divider-pulse{left:398px;width:50px;height:42px;border-radius:6px;background:var(--pulse);opacity:.8}
.action{left:121px;font-size:20px;line-height:24px}
.drug{left:509px;font-size:20px;line-height:24px;display:flex;gap:13px;width:570px}
.drug svg{flex:none;width:15px;height:22px;margin-top:1px}
</style>
</head>
<body>
<div class="abs pulse pulse-left" role="img" aria-label="Heartbeat trace ornament"></div>
<div class="abs pulse pulse-right" role="img" aria-label="Heartbeat trace ornament"></div>

<h1 class="abs title">HYPERTENSI<span class="title-mark" role="img" aria-label="Heart lettering ornament standing in for the letter O"></span>N, ACUTE</h1>
<p class="abs subtitle">Sustained high blood pressure refractory to treating reversible causes</p>

<div class="abs side-band"></div>
<div class="abs side-title">HYPERTENSI<span class="title-mark" role="img" aria-label="Heart lettering ornament standing in for the letter O"></span>N, ACUTE</div>
<div class="abs revision">Revision Feb 2020</div>

<div class="abs child-icon" role="img" aria-label="Child icon with raised arms and a heart"></div>
<p class="abs peds"><b>In pediatrics,</b> hypertension is almost always treated by addressing likely causes such as light anesthesia or measurement error:</p>

<div class="abs tip-icon lime" style="left:112px;top:207px">
  <svg width="44" height="34" viewBox="0 0 44 34" fill="none" stroke="var(--white)" stroke-width="2.5"><rect x="2" y="4" width="24" height="16" rx="4" fill="var(--white)"/><circle cx="37" cy="8" r="4"/><path d="M37 12 V24 H22 V30 H32"/></svg>
</div>
<div class="abs tip-text lime" style="top:207px">Ensure correct BP cuff size: cuff bladder width ~ 40% of limb circumference</div>
<div class="abs tip-icon green" style="left:112px;top:271px">
  <svg width="58" height="40" viewBox="0 0 58 40" fill="none" stroke="#111" stroke-width="1.5"><path d="M30 34 C16 24 12 18 12 12 C12 6 17 3 21 3 C25 3 28 5 30 9 C32 5 35 3 39 3 C44 3 48 6 48 12 C48 18 44 24 30 34Z" fill="var(--white)" stroke="none"/><line x1="4" y1="36" x2="56" y2="36"/><line x1="6" y1="36" x2="52" y2="6"/></svg>
</div>
<div class="abs tip-text green" style="top:271px">Ensure arterial line transducer is at level of heart</div>
<p class="abs note">-Consider placing arterial line if not already present</p>

<div class="abs bp-head">Hypertensive Blood Pressure Range<span>*</span></div>
<div class="abs bp-table">
  <div class="bp-row"><div class="r-head">Age (yr)</div><div class="r-head">Systolic</div><div class="r-head">Diastolic</div></div>
  <div class="bp-row"><div class="r1">newborn</div><div class="r1">&gt;97</div><div class="r1">&gt;70</div></div>
  <div class="bp-row"><div class="r2">1-3</div><div class="r2">&gt;105</div><div class="r2">&gt;61</div></div>
  <div class="bp-row"><div class="r3">4-12</div><div class="r3">&gt;113</div><div class="r3">&gt;86</div></div>
</div>

<div class="abs caution-label">* CAUTION:</div>
<p class="abs caution">Anti-hypertensive drugs are almost never needed for routine pediatric cases. These medications are used almost exclusively for specialized cardiac, neurosurgical, or endocrine (pheochromocytoma) cases. Consult an expert before use. Rule-out increased ICP.</p>

<div class="abs panel action-panel"></div>
<div class="abs panel drug-panel"></div>
<div class="abs pill action-head">Action</div>
<div class="abs pill drug-head">Drug (IV Dosing)</div>

<div class="abs divider" style="top:612px"></div>
<div class="abs divider-pulse" style="top:591px" role="img" aria-label="Heartbeat trace ornament"></div>
<div class="abs divider" style="top:735px"></div>
<div class="abs divider-pulse" style="top:714px" role="img" aria-label="Heartbeat trace ornament"></div>
<div class="abs divider" style="top:818px"></div>
<div class="abs divider-pulse" style="top:797px" role="img" aria-label="Heartbeat trace ornament"></div>

<div class="abs action" style="top:551px">Direct smooth muscle<br>relaxation</div>
<div class="abs action" style="top:662px">β-Adrenergic blockade</div>
<div class="abs action" style="top:768px">Calcium channel blockade</div>
<div class="abs action" style="top:829px">D1-dopamine agonist</div>

<div class="abs drug" style="top:544px"><svg viewBox="0 0 15 22"><path d="M7.5 0 C10 7 15 11 15 15 A7.5 7 0 0 1 0 15 C0 11 5 7 7.5 0Z" fill="var(--red)"/></svg><span>Sodium nitroprusside 0.5-10 MICROgrams/kg/min</span></div>
<div class="abs drug" style="top:580px"><svg viewBox="0 0 15 22"><path d="M7.5 0 C10 7 15 11 15 15 A7.5 7 0 0 1 0 15 C0 11 5 7 7.5 0Z" fill="var(--red)"/></svg><span>HydrALAZINE 0.1-0.2 mg/kg (adult dose 5-10 mg)</span></div>
<div class="abs drug" style="top:625px"><svg viewBox="0 0 15 22" style="margin-top:12px"><path d="M7.5 0 C10 7 15 11 15 15 A7.5 7 0 0 1 0 15 C0 11 5 7 7.5 0Z" fill="var(--red)"/></svg><span>Esmolol 100-500 MICROgrams/kg over 5 min, then 25-300 MICROgrams/kg/min</span></div>
<div class="abs drug" style="top:679px"><svg viewBox="0 0 15 22" style="margin-top:12px"><path d="M7.5 0 C10 7 15 11 15 15 A7.5 7 0 0 1 0 15 C0 11 5 7 7.5 0Z" fill="var(--red)"/></svg><span>Labetalol (also α effect) 0.2-1 mg/kg q 10 min; 0.4-3 mg/kg/<i>hour</i> (infusion)</span></div>
<div class="abs drug" style="top:751px"><svg viewBox="0 0 15 22"><path d="M7.5 0 C10 7 15 11 15 15 A7.5 7 0 0 1 0 15 C0 11 5 7 7.5 0Z" fill="var(--red)"/></svg><span>niCARdapine 0.5-5 MICROgrams/kg/min</span></div>
<div class="abs drug" style="top:785px"><svg viewBox="0 0 15 22"><path d="M7.5 0 C10 7 15 11 15 15 A7.5 7 0 0 1 0 15 C0 11 5 7 7.5 0Z" fill="var(--red)"/></svg><span>Clevidipine 0.5-3.5 MICROgrams/kg/min</span></div>
<div class="abs drug" style="top:836px"><svg viewBox="0 0 15 22"><path d="M7.5 0 C10 7 15 11 15 15 A7.5 7 0 0 1 0 15 C0 11 5 7 7.5 0Z" fill="var(--red)"/></svg><span>Fenoldopam 0.2-0.8 MICROgrams/kg/min</span></div>
</body>
</html>
```